Brand New Church Business Card Design. Needs to appeal to high school students, professionals.

Business Card. Bold lines and colors. Simple font. This is a new church looking to attract new families who have moved to the area. Business professionals mostly. have a working logo. may need a little tweaking. Church is designed to do excellent ministries for students and children. Like business card design in box on mark vault homepage. Want a front and back side. Prefer colors to match the logo. But will lean on designers preferences and wisdom. DO NOT WANT A CROSS OR RELIGIOUS SYMBOL on the card.

Target Market(s)

Families, Professionals, Students

Industry/Entity Type

High School

Contact Information for Business Card

SaltRock ChurchSaltRock.atForrest Coulter904-515-8349Forrest@PineHollow.at

Font styles to use
Sans Serif

Colors
0255a3
ffffff

Requirements
Must have
• Bold colors. Very Masculine. Creative
Nice to have
• On printnook.markvault.com homepage in the business card design box. the card with the black, blue and gray looks really sharp. matches our logos.
Should not have
• no crosses or religious symbols.

```html
<!DOCTYPE html>
<html lang="en">
<head>
<meta charset="utf-8">
<title>PineHollow Church — Business Card</title>
<link href="https://fonts.googleapis.com/css2?family=Lato:wght@400;700;900&display=swap" rel="stylesheet">
<style>
  :root {
    --canvas: #e9e6e1;
    --card: #050505;
    --brand-blue: #1f6fbf;
    --ghost: #16181c;
    --text-light: #d9d9d9;
    --text-muted: #b8b8b8;
  }
  * { box-sizing: border-box; margin: 0; padding: 0; }
  html, body {
    width: 1200px; height: 900px; overflow: hidden;
    background: var(--canvas);
    font-family: "Lato", Arial, sans-serif;
  }
  .canvas {
    width: 1200px; height: 900px;
    display: flex; flex-direction: column;
    align-items: center; justify-content: center; gap: 40px;
  }
  .card {
    position: relative; width: 700px; height: 400px;
    background: var(--card); overflow: hidden;
    box-shadow: 0 10px 28px rgba(0,0,0,.25);
  }
  /* front */
  .card-front .ghost-circle {
    position: absolute; right: 20px; top: -70px;
    width: 330px; height: 330px; border-radius: 50%;
    background: var(--ghost);
  }
  .brand {
    position: absolute; left: 70px; top: 118px;
    display: flex; align-items: center; gap: 14px;
  }
  .brand-dot {
    width: 62px; height: 62px; border-radius: 50%;
    background: var(--brand-blue);
  }
  .brand-name {
    color: var(--brand-blue); font-weight: 900; font-size: 30px; letter-spacing: -0.5px;
  }
  .holder {
    position: absolute; left: 140px; top: 214px;
    color: var(--text-light); font-size: 19px; font-weight: 400; letter-spacing: 0.5px;
    text-transform: uppercase;
  }
  .contacts {
    position: absolute; left: 140px; top: 256px; list-style: none;
    display: flex; flex-direction: column; gap: 9px;
  }
  .contact {
    display: flex; align-items: center; gap: 12px;
    color: var(--text-muted); font-size: 14px;
  }
  .contact svg { width: 14px; height: 14px; fill: var(--brand-blue); stroke: var(--brand-blue); }
  /* back */
  .card-back {
    display: flex; flex-direction: column; align-items: center; justify-content: center; gap: 22px;
  }
  .back-circle {
    width: 200px; height: 200px; border-radius: 50%; background: var(--brand-blue);
  }
  .back-name {
    color: var(--brand-blue); font-weight: 900; font-size: 28px; letter-spacing: -0.5px;
  }
</style>
</head>
<body>
<main class="canvas">
  <section class="card card-front" aria-label="Card front">
    <div class="ghost-circle"></div>
    <div class="brand">
      <div class="brand-dot"></div>
      <span class="brand-name">PineHollow Church</span>
    </div>
    <p class="holder">Dwayne Pellish</p>
    <ul class="contacts">
      <li class="contact">
        <svg viewBox="0 0 16 16"><path stroke="none" d="M3 2h3l1.5 3.5-2 1.3a8 8 0 0 0 3.7 3.7l1.3-2L14 10v3a1 1 0 0 1-1 1A11 11 0 0 1 2 3a1 1 0 0 1 1-1z"/></svg>
        <span>904-555-0172</span>
      </li>
      <li class="contact">
        <svg viewBox="0 0 16 16"><path stroke="none" d="M1 3h14v10H1z"/><path fill="none" stroke="#050505" stroke-width="1.4" d="M1 3.5l7 5.5 7-5.5"/></svg>
        <span>Dwayne@PineHollow.at</span>
      </li>
      <li class="contact">
        <svg viewBox="0 0 16 16"><g fill="none" stroke-width="1.8"><rect x="2" y="7" width="7" height="4" rx="2" transform="rotate(-45 5.5 9)"/><rect x="7" y="5" width="7" height="4" rx="2" transform="rotate(-45 10.5 7)"/></g></svg>
        <span>PineHollow.at</span>
      </li>
    </ul>
  </section>
  <section class="card card-back" aria-label="Card back">
    <div class="back-circle"></div>
    <span class="back-name">PineHollow Church</span>
  </section>
</main>
</body>
</html>
```